Non fiction book cover. The book advises how to get a new job.

The book size will be 20cm high by 13cm wide and I need a front cover which can wrap around to the back. This book has a serious message, but I've tried to make it quite light to read and accessible. So I don't want a cover that is too dour or serious and not frivolous either. At the end of the project, I will need a high resolution 3D image of the book, included as part of the package.<br/>The Title of the book is:- "Past Your Prime? Hunting for the Next Role?<br/>by Gerald Whitcombe-Prynne".<br/>I am thinking of a light yellow background, with a striking image to attract attention. The image and words should be clear and sharp.<br/>Here is the, BACK COVER wording.<br/>"This book tells you clearly and simply the steps that you need to take, to get a job, once you’re over 50.<br/>It advises you on the techniques to use to write a killer CV.<br/>It explains how to ensure that your CV attention.<br/>It shows the best way to approach your local job agency.<br/>It demonstrates the best way to use your network.<br/><br/>This book, written by someone with 30 years’ experience in the recruitment industry, gives you ALL the answers.<br/>Whether you are a top executive or someone after some local part time work, then this book is for you. <br/>With the help of this book you will secure your next position.<br/>

Target Market(s)

UK, over 50s, male and female.

Font styles to use
Serif

Colors
fbee3e

Requirements
Must have
• A clear uncluttered cover.
Should not have
• Fussy and over complicated

```html
<!DOCTYPE html>
<html lang="en">
<head>
<meta charset="utf-8">
<title>Past Your Prime? Hunting for the Next Role? – Book Cover Wrap</title>
<link rel="stylesheet" href="https://fonts.googleapis.com/css2?family=Jost:wght@500;600;700&display=swap">
<style>
  :root {
    --cover-yellow: #f7ea48;
    --ink: #000000;
  }
  html, body {
    margin: 0;
    padding: 0;
    overflow: hidden;
    background: var(--cover-yellow);
  }
  .cover-wrap {
    position: relative;
    width: 1200px;
    height: 800px;
    background: var(--cover-yellow);
    color: var(--ink);
    font-family: "Jost", "Futura", sans-serif;
    font-weight: 600;
    text-transform: uppercase;
    overflow: hidden;
  }

  /* Back cover */
  .back-blurb {
    position: absolute;
    left: 80px;
    top: 88px;
    width: 360px;
    text-align: center;
    font-size: 17.5px;
    line-height: 22.6px;
    letter-spacing: -0.3px;
  }
  .back-blurb p {
    margin: 0 0 23px;
  }
  .rule {
    position: absolute;
    top: 694px;
    height: 5px;
    background: var(--ink);
  }
  .rule--back { left: 83px; width: 354px; }
  .rule--spine { left: 552px; width: 101px; }
  .rule--front { left: 790px; width: 300px; }

  /* Spine */
  .spine-title {
    position: absolute;
    left: 560px;
    top: 88px;
    height: 550px;
    writing-mode: vertical-rl;
    font-weight: 700;
    font-size: 40px;
    line-height: 41px;
    letter-spacing: -0.5px;
    white-space: nowrap;
  }
  .spine-author {
    position: absolute;
    left: 545px;
    top: 710px;
    width: 115px;
    text-align: center;
    font-size: 11px;
    line-height: 14px;
    font-weight: 600;
  }

  /* Front cover */
  .front-title {
    position: absolute;
    inset: 0;
    width: 1200px;
    height: 800px;
  }
  .front-title text {
    font-family: "Jost", "Futura", sans-serif;
    font-weight: 700;
    fill: var(--ink);
  }
  .front-author {
    position: absolute;
    left: 780px;
    top: 706px;
    width: 320px;
    text-align: center;
    font-size: 22px;
    line-height: 28px;
    letter-spacing: -0.4px;
    white-space: nowrap;
  }
</style>
</head>
<body>
  <main class="cover-wrap">
    <section class="back-cover">
      <div class="back-blurb">
        <p>This book tells you clearly and simply the steps that you need to take, to get a job, once you’re over 50.</p>
        <p>It advises you on the techniques to use to write a killer CV.</p>
        <p>It explains how to ensure that your CV attention.</p>
        <p>It shows the best way to approach your local job agency.</p>
        <p>It demonstrates the best way to use your network.</p>
        <p>This book, written by someone with 30 years’ experience in the recruitment industry, gives you all the answers. Whether you are a top executive or someone after some local part time work, then this book is for you. With the help of this book you will secure your next position.</p>
      </div>
      <div class="rule rule--back"></div>
    </section>

    <section class="spine">
      <div class="spine-title">Past Your | Hunting For<br>Prime? | The Next Role?</div>
      <div class="rule rule--spine"></div>
      <div class="spine-author">By<br>Gerald<br>Whitcombe-Prynne</div>
    </section>

    <section class="front-cover">
      <svg class="front-title" viewBox="0 0 1200 800" aria-label="Past Your Prime? Hunting for the Next Role?">
        <text x="732" y="170" font-size="106" textLength="416" lengthAdjust="spacingAndGlyphs">PAST YOUR</text>
        <text x="732" y="305" font-size="124" textLength="416" lengthAdjust="spacingAndGlyphs">PRIME?</text>
        <text x="732" y="380" font-size="62" textLength="416" lengthAdjust="spacingAndGlyphs">HUNTING FOR</text>
        <text x="732" y="490" font-size="100" textLength="416" lengthAdjust="spacingAndGlyphs">THE NEXT</text>
        <text x="732" y="635" font-size="148" textLength="416" lengthAdjust="spacingAndGlyphs">ROLE?</text>
      </svg>
      <div class="rule rule--front"></div>
      <div class="front-author">By Gerald Whitcombe-Prynne</div>
    </section>
  </main>
</body>
</html>
```